Veteran Owned General Contractor needs Bold New Business Cards

We are a service disabled veteran owned small business. We're a general contractor that specializes in excavation, underground utilities, site work, land clearing and demolition. We would like a fresh, simple, bold, new look for our business cards. We're open to ideas! We'd like to incorporate the following information on the card:

Company Name & Logo, Name of Person, Job Title, Office Phone, Fax, Cell Phone, Email Address, Website, SDVOSB

Our logo is included. We look forward to your thoughts.

Thank you!
Updates

Reason: Hello Due to the overwhelming response to this project, we are extending the deadline one time to allow for improved communication and feedback with the top candidates. We would like to thank everyone for their hard work and exceptional creativity! Thank you

Industry/Entity Type

Business

Contact Information for Business Card

Font styles to use
Sans Serif

Requirements
Nice to have
• As we are a veteran owned company, it would be nice to incorporate an American flag into the design. Maybe on the back?

```html
<!DOCTYPE html>
<html lang="en">
<head>
<meta charset="utf-8">
<title>Bedrock 9 Inc – Business Cards</title>
<link rel="stylesheet" href="https://fonts.googleapis.com/css2?family=Open+Sans:wght@400;600;700&display=swap">
<style>
  :root {
    --page: #d6d6d6;
    --card-black: #231f20;
    --brand-green: #6cc04a;
    --steel-grey: #8a8b8d;
    --paper-white: #ffffff;
    --text-light: #f2f2f2;
  }
  * { box-sizing: border-box; margin: 0; padding: 0; }
  html, body {
    width: 1200px; height: 1200px; overflow: hidden;
    background: var(--page);
    font-family: "Open Sans", sans-serif;
  }
  .sheet {
    width: 1200px; height: 1200px;
    display: flex; flex-direction: column; align-items: center; justify-content: center;
    gap: 56px;
  }
  .card {
    position: relative;
    width: 900px; height: 514px;
    box-shadow: 0 10px 30px rgba(0,0,0,.25);
    overflow: hidden;
  }
  /* Front */
  .card--front {
    background: var(--card-black);
    display: flex; align-items: center; justify-content: center;
  }
  .brand {
    display: flex; align-items: center; gap: 22px;
  }
  .brand__square {
    width: 58px; height: 58px;
    background: var(--steel-grey);
    border-radius: 8px;
  }
  .brand__name {
    color: var(--brand-green);
    font-weight: 700;
    font-size: 64px;
    letter-spacing: 3px;
    text-transform: uppercase;
  }
  /* Back */
  .card--back { background: var(--paper-white); }
  .card__shape { position: absolute; inset: 0; }
  .contact {
    position: absolute; left: 120px; top: 190px;
    color: var(--text-light);
  }
  .contact__name {
    color: var(--brand-green);
    font-weight: 600; font-size: 34px; line-height: 1.1;
  }
  .contact__title { font-size: 21px; margin-bottom: 26px; }
  .contact__address { font-size: 19px; line-height: 1.3; margin-bottom: 24px; padding-left: 36px; }
  .contact__list { list-style: none; font-size: 19px; line-height: 1.4; padding-left: 64px; }
  .contact__list li { display: flex; align-items: center; gap: 12px; }
  .contact__list svg { width: 18px; height: 18px; fill: var(--brand-green); flex: none; }
  .badge {
    position: absolute; left: 585px; top: 107px;
    width: 300px; height: 300px;
    background: var(--card-black);
    border-radius: 40px;
    display: flex; align-items: center; justify-content: center;
    text-align: center;
  }
  .badge__name {
    color: var(--brand-green);
    font-weight: 700; font-size: 40px; line-height: 1.15;
    letter-spacing: 2px; text-transform: uppercase;
  }
</style>
</head>
<body>
<main class="sheet">
  <section class="card card--front">
    <div class="brand">
      <span class="brand__square"></span>
      <span class="brand__name">Bedrock 9 Inc</span>
    </div>
  </section>

  <section class="card card--back">
    <svg class="card__shape" viewBox="0 0 900 514" aria-hidden="true">
      <path d="M0 36 L590 36 C530 130 530 390 590 478 L0 478 Z" fill="var(--card-black)"/>
    </svg>

    <div class="contact">
      <p class="contact__name">Daniel Harper</p>
      <p class="contact__title">President</p>
      <p class="contact__address">18 Quarry Road, Stone Field<br>P.O. Box 210, 40 Ridge Avenue</p>
      <ul class="contact__list">
        <li><svg viewBox="0 0 24 24"><path d="M6.6 10.8a15.1 15.1 0 0 0 6.6 6.6l2.2-2.2c.3-.3.7-.4 1-.2 1.1.4 2.3.6 3.6.6.6 0 1 .4 1 1V20c0 .6-.4 1-1 1A17 17 0 0 1 3 4c0-.6.4-1 1-1h3.5c.6 0 1 .4 1 1 0 1.3.2 2.5.6 3.6.1.3 0 .7-.2 1z"/></svg>(555) 014-2271</li>
        <li><svg viewBox="0 0 24 24"><path d="M7 1h10a2 2 0 0 1 2 2v18a2 2 0 0 1-2 2H7a2 2 0 0 1-2-2V3a2 2 0 0 1 2-2zm0 3v14h10V4zm5 15.5a1 1 0 1 0 0 2 1 1 0 0 0 0-2z"/></svg>(555) 014-2289</li>
        <li><svg viewBox="0 0 24 24"><path d="M6 2h12v5H6zM4 8h16a2 2 0 0 1 2 2v7h-4v5H6v-5H2v-7a2 2 0 0 1 2-2zm4 8v4h8v-4z"/></svg>(555) 014-2295</li>
        <li><svg viewBox="0 0 24 24"><path d="M2 5h20v14H2zm2 2v.5l8 5 8-5V7l-8 5z"/></svg>office@bedrocknine.com</li>
      </ul>
    </div>

    <div class="badge">
      <span class="badge__name">Bedrock 9<br>Inc</span>
    </div>
  </section>
</main>
</body>
</html>
```